Flyer Design Project

I am opening a yoga studio called Harbourlight Yoga .Pilates. Fitness
and require a flyer that will be letterbox dropped. It will two sided - DL size.100mm × 210mm

The studio will offer Vinyasa Flow Yoga and Mat Pilates classes. We aim to enable people to lead healthier, happier lives through improved strength, flexibility and general well being that regular yoga and pilates practice offers.

We offer group classes, private and semi private sessions in yoga and pilates.

it must have the logo on it- I have uploaded the logo in two versions - not sure what will look the best.

pick up one of the colours from the logo as the background colour.

Side one:
Simple and clean with one side showing logo and address details, website and with simple intro about studio (if it fits)

Location: 1st Floor, 17 Wattlegrove Parade, Kelsmoor, 3287
phone: 0412 908316
www.harbourlightkelsmoor.com.au

OPENING OCTOBER

other side - class descriptions and intro offer for new clients
$20 for 7 days of classes
$99 for 1 month unlimited.

Class descriptions:
Vinyasa Flow yoga: A class that flows from pose to pose integrating breath, alignment, strength and power. All levels are catered for in a warm room heated to around 26 degrees. You will leave feeling inspired, empowered and energised.

Mat Pilates: A strong, challenging class integrating the key principles of pilates: concentration, control, centring, precision, flowing movement and breath. Using the core as a focus to develop these principles you will be hooked on the physical freedom you experience post workout:improved strength, flexibility and vitality that pilates offers.

Private and semi Private tuition available.

Target Market(s)

mainly women, athletic, 35-55 age, middle class, well educated

Industry/Entity Type

Fitness

Requirements
Must have
• 2 pages
the logo

Should not have
• no pics

```html
<!DOCTYPE html>
<html lang="en">
<head>
<meta charset="utf-8">
<title>Harbourlight Yoga – DL Flyer</title>
<link rel="stylesheet" href="https://fonts.googleapis.com/css2?family=Great+Vibes&family=Questrial&family=Patrick+Hand&family=Lato:wght@700&display=swap">
<style>
:root{
  --page:#ffffff;
  --panel-edge:#8a8a8a;
  --teal:#2b7b6c;
  --cyan:#4dd2e3;
  --red:#e3212b;
  --script-red:#d8262f;
  --ink:#333333;
  --grey:#4a4a4a;
  --orange:#f39a2c;
  --orange-soft:#fbd8a6;
  --sky:#cfeef3;
}
*{margin:0;padding:0;box-sizing:border-box}
html,body{width:1153px;height:1200px;overflow:hidden;background:var(--page)}
.canvas{position:relative;width:1153px;height:1200px}
.panel{position:absolute;top:41px;height:1126px;border:1px solid var(--panel-edge);overflow:hidden;background:#fff}
.panel--front{left:23px;width:537px}
.panel--back{left:587px;width:536px}
.txt{position:absolute}

/* plain bands and soft background areas */
.top-band{position:absolute;left:150px;top:0;width:387px;height:8px;background:linear-gradient(90deg,#fff,var(--red))}
.soft-area{position:absolute}
.soft-area--top{left:0;top:20px;width:537px;height:300px;background:radial-gradient(ellipse at 10% 20%,var(--sky),rgba(255,255,255,0) 60%)}
.soft-area--lower{left:0;top:560px;width:537px;height:535px;background:radial-gradient(ellipse at 85% 55%,rgba(243,154,44,.45),rgba(251,216,166,.35) 45%,rgba(255,255,255,0) 75%)}

.title{left:168px;top:36px;font-family:"Great Vibes",cursive;font-size:48px;line-height:60px;color:var(--grey)}
.intro{left:27px;top:125px;width:487px;font-family:"Questrial",sans-serif;font-size:21px;line-height:27.5px;color:var(--teal);text-align:justify;text-indent:36px}
.offer{left:44px;top:288px;width:450px;text-align:center;font-family:"Patrick Hand",cursive;font-size:21px;line-height:27px;text-transform:uppercase;color:var(--grey)}
.opening{left:20px;top:358px;width:492px;text-align:center;font-family:"Patrick Hand",cursive;font-size:42px;line-height:46px;text-transform:uppercase;color:var(--cyan)}
.opening-note{left:20px;top:405px;width:492px;text-align:center;font-family:"Patrick Hand",cursive;font-size:14px;line-height:20px;text-transform:uppercase;color:var(--grey)}
.price{left:20px;width:506px;text-align:center;font-family:"Patrick Hand",cursive;font-size:28px;line-height:32px;text-transform:uppercase;color:var(--red)}
.price--week{top:430px}
.price--month{top:462px}

.section-band{position:absolute;left:0;top:518px;width:240px;height:36px;background:linear-gradient(90deg,var(--orange),var(--orange-soft) 65%,rgba(255,255,255,0))}
.section-title{left:18px;top:523px;font-family:"Questrial",sans-serif;font-size:21px;line-height:26px;color:var(--grey)}
.class-name{left:20px;font-family:"Great Vibes",cursive;font-size:32px;line-height:40px;color:var(--script-red)}
.class-name--yoga{top:557px}
.class-name--pilates{top:724px}
.class-copy{left:25px;width:489px;font-family:"Questrial",sans-serif;font-size:19.5px;line-height:24.6px;color:var(--ink);text-align:justify;text-indent:50px}
.class-copy--yoga{top:593px}
.class-copy--pilates{top:759px}
.tuition{left:25px;top:959px;font-family:"Questrial",sans-serif;font-size:19.5px;line-height:24px;color:var(--ink)}

.brand-dot{position:absolute;border-radius:50%;background:var(--orange)}
.brand-dot--front{left:438px;top:952px;width:66px;height:66px}
.brand-dot--back{left:218px;top:347px;width:100px;height:100px}
.brand-name{font-family:"Lato",sans-serif;font-weight:700;color:var(--grey);letter-spacing:.5px}
.brand-name--front{right:12px;top:1038px;font-size:18px;line-height:21px;text-align:right}
.brand-name--back{left:0;top:452px;width:100%;font-size:20px;line-height:24px;text-align:center}

.footer-band{position:absolute;left:0;bottom:0;width:100%;height:31px;background:linear-gradient(90deg,#fbd3a3,var(--orange) 45%,var(--red))}
.footer-web{right:16px;bottom:7px;font-family:"Questrial",sans-serif;font-weight:700;font-size:14px;line-height:17px;color:#fff}
.contact{left:0;top:498px;width:100%;text-align:center;font-family:"Lato",sans-serif;font-weight:700;font-style:normal;font-size:15.5px;line-height:21.5px;color:var(--ink)}
</style>
</head>
<body>
<main class="canvas">
  <section class="panel panel--front" aria-label="Front: studio intro and class descriptions">
    <div class="soft-area soft-area--top" role="img" aria-label="Soft light blue background artwork"></div>
    <div class="soft-area soft-area--lower" role="img" aria-label="Soft warm orange background artwork"></div>
    <div class="top-band"></div>
    <h1 class="txt title">Harbourlight Yoga</h1>
    <p class="txt intro">The studio will offer Vinyasa Flow Yoga and Mat Pilates classes. We aim to enable people to lead healthier, happier lives through improved strength, flexibility and general well being that regular yoga and pilatespractice offers.</p>
    <p class="txt offer">We offer group classes, private and semi private sessions in yoga and pilates.</p>
    <p class="txt opening">Opening October</p>
    <p class="txt opening-note">Class descriptions and intro offer for new clients</p>
    <p class="txt price price--week">$20 for 7 days of classes</p>
    <p class="txt price price--month">$99 for 1 month unlimited.</p>
    <div class="section-band"></div>
    <h2 class="txt section-title">Class descriptions:</h2>
    <h3 class="txt class-name class-name--yoga">Vinyasa Flow yoga:</h3>
    <p class="txt class-copy class-copy--yoga">A class that flows from pose to pose integrating breath, alignment, strength and power. All levels are catered for in a warm room heated to around 26 degrees. You will leave feeling inspired, empowered and energised.</p>
    <h3 class="txt class-name class-name--pilates">Mat Pilates:</h3>
    <p class="txt class-copy class-copy--pilates">A strong, challenging class integrating the key principles of pilates: concentration, control, centring, precision, flowing movement and breath. Using the core as a focus to develop these principles you will be hooked on the physical freedom you experience post workout:&nbsp; improved strength, flexibility and vitality that pilates offers.</p>
    <p class="txt tuition">Private and semi Private tuition available.</p>
    <span class="brand-dot brand-dot--front"></span>
    <p class="txt brand-name brand-name--front">HARBOURLIGHT YOGA<br>.PILATES. FITNESS</p>
    <div class="footer-band"></div>
    <p class="txt footer-web">www.harbourlightkelsmoor.com.au</p>
  </section>

  <section class="panel panel--back" aria-label="Back: studio name and contact details">
    <span class="brand-dot brand-dot--back"></span>
    <p class="txt brand-name brand-name--back">HARBOURLIGHT YOGA<br>.PILATES. FITNESS</p>
    <address class="txt contact">
      Location: 1st Floor, 17 Wattlegrove<br>
      Parade, Kelsmoor, 3287<br>
      phone: 0412 908316<br>
      www.harbourlightkelsmoor.com.au
    </address>
  </section>
</main>
</body>
</html>
```